Brindo like IOS/Android app for Okinawa Island - LumaTrail

LumaTrail is the name of the app
The closest thing that I can relate this app to is a region specific Brindo app. The app is for the island of Okinawa and is geared towards English speaking travelers. The style of app that I prefer is a look and feel similar to that of the new Nestora app, color should also be similar if not the same as the nestora app.

The app needs to have the following screens

LOGIN SCREEN
1. App login page with a login for chatterly button or create an account option. Personally I would like an image in the background with a real beachy feel, but don't do this if it messes with your design.

2. Depending on the choice of login there will need to be a second login screen to create the account. Nestora does this nicely.

PRIMARY HOME
primary page similar to the primary layout when you get into the nestora app.
This page is kind of like the home page of the app and should include the following items:
search field
upcoming events
popular things to do
featured restaurants
Featured Places to stay
area guides
Moving here
(this will allow the person to select, housing agencies, auto dealers, schools etc) These are essentially just quick searches.
Each selection should be listed so that the user can swipe to the left or right in order to view more listings under the categories listed above. It will not be the full list but rather a sample.

SIDEBAR POPOUT MENU
Popout sidebar that contains the following selections
Places to Eat
Things to do
Attractions
Beaches
Shop
Farmers Markets
Places to Stay
Schools & DayCare
Housing
Auto
Events
Account settings
Add a business

LIST VIEW
4. List view page for whatever category the user selected. This will show all the listings for the specific category: The top should also have the featured listings for that category

INDIVIDUAL LISTING
5. Listing page
This will include photos, description, hours, map(this can be a button to view the map or the map), Reviews with a leave a review option

AREA GUIDES
6. Area Guides. This is where the user will be able to select a specific area and learn about it. It should include an area where there can be a description, photos with a hero photo image, a map, popular local attractions or things to do, best restaurants in the area, places to stay etc.

PROFILE PAGE
7. Profile page for the user where they can make any updates they need to

Every page but the listing page should include the search bar. When the user clicks in it they should be able to see a drop down of quick select searches or run a regular search.

Logo
I have attached a logo that was made that needs a redesign. The map marker contains the logo for Okinawa within it so it does need to be similar.

If you have any questions or need clarification please send me a message. I will respond promptly.
Thank you,

```html
<!DOCTYPE html>
<html lang="en">
<head>
<meta charset="utf-8">
<title>LumaTrail – Welcome and Login Screens</title>
<link href="https://fonts.googleapis.com/css2?family=Montserrat:wght@400;500;600;800&display=swap" rel="stylesheet">
<style>
  :root {
    --page-bg: #f2f3f5;
    --coral: #ff5a5f;
    --chatterly-blue: #3b5aa8;
    --white: #ffffff;
    --sky-top: #6f96d8;
    --sky-mid: #9fc0e8;
    --hill: #3f6b5a;
    --sea-light: #3cc7c4;
    --sea-deep: #1c8f96;
    --night-top: #2a3552;
    --lagoon: #2a6f72;
    --jungle: #24401f;
    --jungle-deep: #162a14;
  }
  * { box-sizing: border-box; margin: 0; padding: 0; }
  html, body {
    width: 1200px; height: 1200px; overflow: hidden;
    background: var(--page-bg);
    font-family: "Montserrat", Arial, sans-serif;
  }
  .screens {
    position: absolute; inset: 0;
    display: flex; justify-content: center; align-items: center; gap: 80px;
  }
  .screen {
    position: relative; width: 400px; height: 706px; overflow: hidden;
    color: var(--white);
    box-shadow: 0 20px 50px rgba(0,0,0,0.15);
  }
  .backdrop { position: absolute; inset: 0; }
  .backdrop--coast {
    background: linear-gradient(180deg, var(--sky-top) 0%, var(--sky-mid) 24%, var(--hill) 30%, var(--hill) 38%, var(--sea-light) 55%, var(--sea-deep) 80%, var(--sea-light) 100%);
  }
  .backdrop--island {
    background: linear-gradient(180deg, var(--night-top) 0%, #3b4a5e 18%, var(--jungle) 26%, var(--lagoon) 36%, #1f5f63 56%, var(--jungle) 68%, var(--jungle-deep) 100%);
  }
  .status-bar {
    position: absolute; top: 0; left: 0; right: 0; height: 26px;
    display: flex; justify-content: space-between; align-items: center;
    padding: 0 8px; font-size: 12px; font-weight: 500;
  }
  .status-bar .battery {
    display: inline-block; width: 22px; height: 9px; border: 1px solid var(--white);
    margin-left: 4px; vertical-align: -1px; position: relative;
  }
  .status-bar .battery::before {
    content: ""; position: absolute; left: 1px; top: 1px; bottom: 1px; width: 4px; background: var(--white);
  }
  .headline {
    position: absolute; left: 30px; top: 180px;
    font-weight: 800; font-size: 43px; line-height: 55px; letter-spacing: 2px;
    text-transform: uppercase;
  }
  .pager {
    position: absolute; top: 586px; left: 0; right: 0;
    display: flex; justify-content: center; gap: 14px;
  }
  .pager span { width: 13px; height: 13px; border-radius: 50%; background: rgba(255,255,255,0.45); }
  .pager span.is-active { background: var(--white); }
  .action-bar {
    position: absolute; left: 0; right: 0; bottom: 0; height: 54px;
    background: var(--coral); display: flex; align-items: center;
    font-size: 19px; font-weight: 400;
  }
  .action-bar a { flex: 1; text-align: center; color: var(--white); text-decoration: none; letter-spacing: 0.5px; }
  .action-bar .divider { width: 1px; height: 34px; background: rgba(255,255,255,0.8); }
  .brand-dot {
    position: absolute; left: 163px; top: 100px;
    width: 74px; height: 74px; border-radius: 50%; background: var(--coral);
  }
  .brand-name {
    position: absolute; left: 0; right: 0; top: 218px;
    text-align: center; font-size: 46px; font-weight: 600; letter-spacing: 0.5px; line-height: 60px;
  }
  .auth-button {
    position: absolute; left: 20px; width: 358px; height: 54px;
    display: flex; align-items: center; justify-content: center;
    font-size: 17px; font-weight: 500; letter-spacing: 0.8px; color: var(--white);
  }
  .auth-button--chatterly { top: 370px; background: var(--chatterly-blue); padding-left: 54px; }
  .auth-button--chatterly::before {
    content: ""; position: absolute; left: 54px; top: 0; bottom: 0; width: 1px; background: rgba(0,0,0,0.2);
  }
  .auth-button--email { top: 448px; background: var(--coral); padding-left: 54px; }
  .auth-button--email svg { position: absolute; left: 13px; top: 17px; }
  .auth-button--signup { top: 526px; height: 52px; border: 1px solid rgba(255,255,255,0.85); font-weight: 600; }
</style>
</head>
<body>
<main class="screens">

  <section class="screen screen--welcome">
    <div class="backdrop backdrop--coast" role="img" aria-label="Photo of a turquoise lagoon with green hills and white boats on the water"></div>
    <div class="status-bar">
      <span>●●●○○ ORBITA</span><span>4:21 PM</span><span>22% <i class="battery"></i></span>
    </div>
    <h1 class="headline">Every day is<br>a journey,<br>and the<br>journey<br>itself is<br>home</h1>
    <div class="pager"><span class="is-active"></span><span></span><span></span><span></span></div>
    <nav class="action-bar">
      <a href="#">Sign Up</a><span class="divider"></span><a href="#">Log In</a>
    </nav>
  </section>

  <section class="screen screen--login">
    <div class="backdrop backdrop--island" role="img" aria-label="Photo of a forested island in a lagoon at dusk with tropical palms in the foreground"></div>
    <div class="status-bar">
      <span>●●●○○ ORBITA</span><span>4:21 PM</span><span>22% <i class="battery"></i></span>
    </div>
    <span class="brand-dot"></span>
    <span class="brand-name">LumaTrail</span>
    <a class="auth-button auth-button--chatterly">Log in with Chatterly</a>
    <a class="auth-button auth-button--email">
      <svg width="30" height="20" viewBox="0 0 30 20" fill="none" stroke="#fff" stroke-width="1.3">
        <rect x="0.7" y="0.7" width="28.6" height="18.6"/>
        <path d="M0.7 0.7 L15 11 L29.3 0.7 M0.7 19.3 L11 9 M29.3 19.3 L19 9"/>
      </svg>
      Log in with Email
    </a>
    <a class="auth-button auth-button--signup">Sign Up</a>
  </section>

</main>
</body>
</html>
```